"Valmoria Inc." in Canada Needs a product Label Design" in MULTI-LANGUAGE: English &

We are the first Nutritional company developed "Ultra Fine Oyster Shell Calcium Powder Supplement," the particle size is range between 20 ~80% of 20 ~ 500Nm (nanometer size). Helped cured people suffering from Osteoporosis within a year. Many years of clinical research in Asia, Germany, USA. Now, we've developed unique formulas with a new product name, required "Fresh New Design" for this product.

The product name is: pyrQuelo

Please read attached files carefully, find out function of this product.

The label must be in "Multi-Language Plate Form" design Label: English & French." The Canadian government required both language "Product Label."

So, the designer must be familiar with a multi-language task.

I am uploading benefits of "pyrQuelo," we need a strong and familiar fresh design image, i do not want the label appears like a "Drug", must be creative and unique "MODERN DESIGN" Nutritional Supplement concept. I have attached "FASKEL BRANDS" product for your reference. We would prefered similiar layout design like "Faskel" product design style.

pyrQuelo may:
* HELPS BUILD STRONG BONES AND TEETH
* HELPS PREVENT OSTEOPOROSIS
* HELPS TO FORM RED BLOOD CELLS
* HELPS TO MAINTAIN IMMUNE FUNCTION

Medicinal Ingredients: / Ingrédients médicinaux :
Each (800 mg) capsule contains:
Chaque capsule (800 mg) contient :
Elemental Calcium / calcium élémentaire 200 mg
Phosphorus / phosphore 25 mg
Magnesium / magnésium 30 mg
Zinc / zinc 8 mg
Copper / cuivre 200 mcg
Vanadium / vanadium 8 mcg
Silicon / silicium 700 mcg
Boron / bore 200 mcg
Vitamin / vitamine D 5 mcg

Non-medicinal Ingredients:
Magnesium stearate, Hydroxypropylmethylcellulose,
Microcrystalline cellulose.

Recommended Dose:
Adults: 1~2 capsules daily.

Directions: Take with food, a few hours before or after consuming other
medications/natural health products.

Storage: Store in an airtight container, away from light.

Caution: If you are pregnant or breastfeeding, consult a healthcare professional
prior to use. As with all nutritional products, consult your physician before
using this product if you are taking medication.

Ingrédients non médicinaux :
Stéarate de magnésium, hydroxypropylméthylcellulose,
cellulose microcristalline.

Dose recommandée : Adultes: 1~2 capsules par jour.

Directions : Prendre avec de la nourriture, quelques heures avant ou après
avoir consommé d'autres médicaments / produits de santé naturels.

Stockage : Conserver dans un récipient hermétique, à l'abri de la lumière.

Attention : Si vous êtes enceinte ou allaitez, consultez un professionnel de
la santé avant de l'utiliser. Comme avec tous les produits nutritionnels, consultez
votre médecin avant d'utiliser ce produit si vous prenez des médicaments.

Furthermore, we have a more projects after this.

If you require further question, please contact me soon.

Gareth

Target Market(s)

Nutritional Supplement Industry, Direct Retailer, Wholesale

Industry/Entity Type

Health Product

Colors

Designer to choose colors to be used in the design.

Requirements
Must have
• English & French Language on the label. Canadian product. Please make sure, made in Canada recognizable on the label.
• My intention of designing idea from "Faskel Naturals Label" product, the label represent a clear message, excellent color combination.
• I would like to see a designer who can design "pyrQuelo" label similar fashion creatively, not to copied the same format as a "Faskel Naturals Label". If anyone of you can pull out this project successfully, I will have a few more projects will be awarded.
Nice to have
• What this product label is trying to send out the message. What this product is all about.
Should not have
• The label should not apprears like a "Drug". Do not make a colorful design

```html
<!DOCTYPE html>
<html lang="en">
<head>
<meta charset="utf-8">
<title>pyrQuelo Label</title>
<link rel="stylesheet" href="https://fonts.googleapis.com/css2?family=Barlow:wght@400;500;600;700&display=swap">
<style>
  :root {
    --backdrop: #cfe0f0;
    --label-white: #ffffff;
    --band-red: #e0301a;
    --brand-orange: #f0a21e;
    --text-red: #d8300f;
    --benefit-band: rgba(226, 70, 40, 0.8);
    --benefit-band-fade: rgba(226, 70, 40, 0.15);
    --molecule-orange: #f2a878;
    --molecule-pale: #fbe3d2;
    --benefit-text: #ffffff;
    --benefit-text-soft: #ffe9df;
  }
  * { margin: 0; padding: 0; box-sizing: border-box; }
  html, body { width: 1200px; height: 886px; overflow: hidden; }
  body {
    background: var(--backdrop);
    font-family: "Barlow", Arial, sans-serif;
    position: relative;
  }
  .label {
    position: absolute;
    left: 220px; top: 143px;
    width: 760px; height: 600px;
    background: var(--label-white);
    overflow: hidden;
    box-shadow: 0 6px 24px rgba(40, 70, 110, 0.18);
  }
  .label__band {
    position: absolute; left: 0; right: 0; height: 12px;
    background: var(--band-red);
  }
  .label__band--top { top: 22px; }
  .label__band--bottom { bottom: 22px; height: 14px; }
  .label__molecules {
    position: absolute; left: 0; top: 34px;
    width: 230px; height: 530px;
    background: radial-gradient(ellipse at 15% 40%, var(--molecule-orange) 0%, var(--molecule-pale) 50%, rgba(255,255,255,0) 78%);
  }
  .label__shell {
    position: absolute; left: 250px; top: 300px;
    width: 300px; height: 220px;
    background: radial-gradient(ellipse at 50% 100%, rgba(230,200,190,0.45) 0%, rgba(255,255,255,0) 70%);
  }
  .label__brand {
    position: absolute; left: 0; right: 0; top: 52px;
    text-align: center;
    font-size: 112px; font-weight: 600;
    color: var(--brand-orange);
    line-height: 1;
  }
  .label__subtitle {
    position: absolute; left: 0; right: 0; top: 186px;
    text-align: center;
    font-size: 28px; font-weight: 700;
    color: var(--text-red);
    line-height: 1.08;
  }
  .label__subtitle-fr {
    position: absolute; left: 0; right: 0; top: 256px;
    text-align: center;
    font-size: 17px; font-weight: 600;
    color: var(--text-red);
  }
  .label__benefits {
    position: absolute; left: 0; right: 0; top: 292px;
    height: 210px;
    background: linear-gradient(90deg, var(--benefit-band-fade) 0%, var(--benefit-band) 30%, var(--benefit-band) 85%, var(--benefit-band-fade) 100%);
    list-style: none;
    display: flex; flex-direction: column; justify-content: center; align-items: center;
    gap: 7px;
  }
  .label__benefit {
    text-align: center;
    line-height: 1.15;
  }
  .label__benefit-en {
    display: block;
    color: var(--benefit-text);
    font-size: 19px; font-weight: 500;
    text-transform: uppercase;
  }
  .label__benefit-fr {
    display: block;
    color: var(--benefit-text-soft);
    font-size: 14px; font-weight: 400;
    text-transform: uppercase;
  }
  .label__origin {
    position: absolute; left: 0; right: 0; top: 516px;
    text-align: center;
    font-size: 17px; font-weight: 700;
    color: var(--text-red);
    text-transform: uppercase;
    letter-spacing: 1px;
  }
</style>
</head>
<body>
  <section class="label">
    <div class="label__molecules" role="img" aria-label="Orange molecular lattice illustration of linked spheres"></div>
    <div class="label__shell" role="img" aria-label="Faint oyster shell illustration"></div>
    <div class="label__band label__band--top"></div>
    <h1 class="label__brand">pyrQuelo</h1>
    <p class="label__subtitle">Ultra Fine Oyster Shell Calcium<br>Powder Supplement</p>
    <p class="label__subtitle-fr" lang="fr">Supplément de calcium de coquille d'huître en poudre ultrafine</p>
    <ul class="label__benefits">
      <li class="label__benefit"><span class="label__benefit-en">Helps build strong bones and teeth</span><span class="label__benefit-fr" lang="fr">Aide à former des os et des dents solides</span></li>
      <li class="label__benefit"><span class="label__benefit-en">Helps prevent osteoporosis</span><span class="label__benefit-fr" lang="fr">Aide à prévenir l'ostéoporose</span></li>
      <li class="label__benefit"><span class="label__benefit-en">Helps to form red blood cells</span><span class="label__benefit-fr" lang="fr">Aide à former les globules rouges</span></li>
      <li class="label__benefit"><span class="label__benefit-en">Helps to maintain immune function</span><span class="label__benefit-fr" lang="fr">Aide à maintenir la fonction immunitaire</span></li>
    </ul>
    <p class="label__origin">Made in Canada · <span lang="fr">Fabriqué au Canada</span></p>
    <div class="label__band label__band--bottom"></div>
  </section>
</body>
</html>
```